Webdesign project for healthcare IT company

Home, About, Solution, Contact, and Employment pages.

Please match the designs uploaded for colors and effect.

Please choose appropriate healthcare IT related photos to the content. Be sure to include the content that i've attached in the word document.

Please use the following URLs as reference:

www.morvilcare.example
www.tovrix.example
www.pelmaragree.example

Target Market(s)

healthcare providers, doctors, nurses, c-level executives

Industry/Entity Type

Healthcare

Coding

Coded - Design and coding required

Number of Pages Required

5+ page

Font styles to use
Serif
Sans Serif

Colors
6b449b
0455a3
ffffff
333333
959595

Requirements
Must have
• B2B feel, matches the colors in the uploaded design files, images that can be purchased later that meet the content that I've uploaded

```html
<!DOCTYPE html>
<html lang="en">
<head>
<meta charset="utf-8">
<title>Rousa Technologies</title>
<link href="https://fonts.googleapis.com/css2?family=Montserrat:wght@400;500;600;700&family=Open+Sans:wght@400&display=swap" rel="stylesheet">
<style>
:root{
  --purple:#6b449b;
  --blue:#0455a3;
  --indigo:#2f4ea3;
  --white:#ffffff;
  --ink:#333333;
  --grey:#959595;
  --title-grey:#555555;
  --mist:#eceff6;
  --footer:#1f1f23;
  --card:#f4f4f4;
}
*{margin:0;padding:0;box-sizing:border-box}
html,body{width:1200px;height:2299px;overflow:hidden}
body{font-family:"Montserrat",sans-serif;color:var(--ink);position:relative;background:var(--white)}
.abs{position:absolute}

/* header */
.site-header{position:absolute;left:0;top:0;width:1200px;height:123px;background:rgba(246,247,251,.95);z-index:5;box-shadow:0 2px 6px rgba(0,0,0,.15)}
.brand{position:absolute;left:87px;top:40px;display:flex;align-items:center;gap:12px}
.brand-mark{width:22px;height:22px;background:var(--indigo)}
.brand-name{font-size:27px;font-weight:700;color:var(--indigo);letter-spacing:1px}
.contact{position:absolute;top:18px;display:flex;align-items:center;gap:12px}
.contact .icon{width:36px;height:36px;border-radius:50%;border:2px solid var(--purple);display:flex;align-items:center;justify-content:center}
.contact small{display:block;font-size:10px;color:var(--ink)}
.contact span{display:block;font-size:16px;color:#555}
.nav{position:absolute;top:77px;font-size:15px;color:#555}
.quote-btn{position:absolute;left:961px;top:69px;width:153px;height:36px;background:linear-gradient(90deg,var(--indigo),var(--purple));color:#fff;font-size:14px;font-weight:500;display:flex;align-items:center;justify-content:center;border-radius:2px}

/* hero */
.hero-photo{position:absolute;left:0;top:0;width:1200px;height:805px;
  background:
    radial-gradient(ellipse 330px 300px at 850px 440px,rgba(110,175,200,.75),rgba(80,130,160,.35) 55%,rgba(0,0,0,0) 100%),
    radial-gradient(ellipse 120px 120px at 990px 290px,rgba(190,200,90,.45),rgba(0,0,0,0) 100%),
    linear-gradient(180deg,#9a9ca2 0%,#6c6e74 30%,#3c3d42 65%,#2a2b30 100%)}
.hero-title{position:absolute;left:87px;top:304px;font-size:44px;font-weight:400;line-height:53px;color:#fff}
.hero-text{position:absolute;left:87px;top:424px;width:720px;font-size:17.5px;line-height:27px;color:#fff}
.dots{position:absolute;left:1146px;top:384px}
.dots i{display:block;width:11px;height:11px;border-radius:50%;border:1.5px solid #fff;margin-bottom:7px}
.dots i.on{background:#fff}

/* what we do */
.what-we-do{position:absolute;left:0;top:640px;width:1200px;height:605px;background:linear-gradient(180deg,#e6eaf2,#eef0f6);z-index:-1}
.section-title{position:absolute;left:0;width:1200px;text-align:center;font-size:41px;font-weight:500}
.wwd-text{position:absolute;left:245px;width:710px;text-align:center;font-size:13px;line-height:21px;color:#555}
.read-more{position:absolute;left:524px;top:1109px;width:152px;height:44px;border-radius:5px;background:linear-gradient(90deg,var(--indigo),var(--purple));color:#fff;font-size:15px;font-weight:600;display:flex;align-items:center;justify-content:center}

/* offer */
.offer{position:absolute;left:0;top:1242px;width:1200px;height:646px;background:linear-gradient(90deg,#2c4fa4,var(--purple))}
.card{position:absolute;top:1411px;width:330px;height:391px;background:var(--card);padding:5px}
.card-photo{width:320px;height:218px}
.card h3{font-size:23px;font-weight:500;margin:22px 0 0 22px;color:#222}
.card p{font-size:13px;line-height:21px;margin:8px 21px 0 22px;color:#222}

/* footer */
.site-footer{position:absolute;left:0;top:1888px;width:1200px;height:411px;
  background:
    radial-gradient(ellipse 260px 300px at 260px 120px,rgba(120,110,100,.35),rgba(0,0,0,0) 100%),
    radial-gradient(ellipse 300px 260px at 1000px 200px,rgba(110,90,70,.3),rgba(0,0,0,0) 100%),
    linear-gradient(180deg,#2a2a2e,#1c1c20)}
.nl-title{position:absolute;left:0;top:1951px;width:1200px;text-align:center;font-size:32px;letter-spacing:6px;color:#fff;font-weight:500}
.nl-text{position:absolute;left:405px;top:1999px;width:390px;text-align:center;font-family:"Open Sans",sans-serif;font-size:13px;line-height:20px;color:#fff}
.nl-input{position:absolute;left:303px;top:2055px;width:413px;height:49px;background:#fff;font-size:12px;font-style:italic;color:var(--grey);padding:18px 24px}
.nl-button{position:absolute;left:736px;top:2055px;width:162px;height:49px;background:linear-gradient(90deg,var(--indigo),var(--purple));color:#fff;font-size:17px;font-weight:600;letter-spacing:1.5px;display:flex;align-items:center;justify-content:center}
.social{position:absolute;top:2127px;width:36px;height:36px;border-radius:50%;border:2px solid #fff}
.legal{position:absolute;left:0;top:2205px;width:1200px;text-align:center;font-size:13px;color:#ddd;word-spacing:2px}
</style>
</head>
<body>

<div class="hero-photo" role="img" aria-label="Photo of a professional holding a glowing healthcare technology icon wheel"></div>
<svg class="abs" style="left:0;top:600px" width="1200" height="260" viewBox="0 600 1200 260">
  <defs><linearGradient id="band" x1="0" x2="1"><stop offset="0" stop-color="#2f4ea3"/><stop offset="1" stop-color="#6b449b"/></linearGradient></defs>
  <polygon points="0,644 751,805 1200,659 1200,672 751,805 0,680" fill="url(#band)"/>
  <polygon points="0,680 751,805 1200,672 1200,860 0,860" fill="#e6eaf2"/>
</svg>
<div class="what-we-do"></div>

<header class="site-header">
  <div class="brand"><div class="brand-mark"></div><div class="brand-name">ROUSA</div></div>
  <div class="contact" style="left:659px">
    <div class="icon"><svg width="16" height="16" viewBox="0 0 24 24"><path d="M6 2l4 4-2 3c1 3 4 6 7 7l3-2 4 4-3 4C10 22 2 14 2 5z" fill="#6b449b"/></svg></div>
    <div><small>Call US</small><span>+1 (555) 014-0224</span></div>
  </div>
  <div class="contact" style="left:871px">
    <div class="icon"><svg width="18" height="14" viewBox="0 0 24 18"><rect x="1" y="1" width="22" height="16" rx="2" fill="#6b449b"/><path d="M1 2l11 8 11-8" stroke="#fff" stroke-width="2" fill="none"/></svg></div>
    <div><small>Mail to</small><span>hello@rousatech.example</span></div>
  </div>
  <nav>
    <span class="nav" style="left:447px">Home</span>
    <span class="nav" style="left:539px">About</span>
    <span class="nav" style="left:630px">Solution</span>
    <span class="nav" style="left:737px">Employment</span>
    <span class="nav" style="left:875px">Contact</span>
  </nav>
  <div class="quote-btn">Get a free Quote</div>
</header>

<h1 class="hero-title">It’s time to wake up<br>with Rousa Technologies.</h1>
<p class="hero-text">Disruption isn’t just coming – it’s already here and it’s time to wake up to the new world we live in.&nbsp; Here at Rousa Technologies, we embrace the future that disruption brings and make it our aim to assist the world in embracing this bright future with us.&nbsp; We help bring businesses and people adapt to new approaches to old problems.</p>
<div class="dots"><i class="on"></i><i></i><i></i><i></i></div>

<h2 class="section-title" style="top:874px;color:var(--title-grey)">What we do</h2>
<p class="wwd-text" style="top:934px">We are engineers, problem-solvers, people persons, and a friendly face.&nbsp; We want to solve your problem in a way that won’t break the bank, give headaches, leave you with a smile on your face, and keep you smiling throughout our relationship.</p>
<p class="wwd-text" style="top:1019px">We predominantly work in the healthcare IT industry assisting hospitals and clinics with their IT infrastructure and information workflows.&nbsp; We provide software solutions and interoperability services to connect platforms and give care givers a simple view of patient records.</p>
<div class="read-more">Read More &gt;</div>

<section class="offer"></section>
<h2 class="section-title" style="top:1326px;color:#fff">What we Offer</h2>
<article class="card" style="left:87px">
  <div class="card-photo" role="img" aria-label="Photo of a vintage desktop computer on a wooden desk" style="background:radial-gradient(ellipse 110px 90px at 150px 120px,rgba(236,230,205,.85),rgba(236,230,205,0) 100%),linear-gradient(180deg,#5fc9c3 0%,#6cc5bd 62%,#8a6b4c 80%,#6e5238 100%)"></div>
  <h3>Computer Archeology</h3>
  <p>Need data off a legacy system that you would like to sunset?&nbsp; We can help you with that.</p>
</article>
<article class="card" style="left:435px">
  <div class="card-photo" role="img" aria-label="Photo of a person seated in a waiting room holding a tablet" style="background:radial-gradient(ellipse 70px 110px at 175px 110px,rgba(45,55,85,.75),rgba(45,55,85,0) 100%),linear-gradient(180deg,#e4e4e2 0%,#c9c9c7 55%,#b89a78 78%,#a88866 100%)"></div>
  <h3>Digital Check In</h3>
  <p>Still using clipboards to check people into your facility?&nbsp; Struggling to get that paper-based information into your system?&nbsp; We can help you with that.</p>
</article>
<article class="card" style="left:783px">
  <div class="card-photo" role="img" aria-label="Photo of a 3D printer printing a pink object" style="background:radial-gradient(ellipse 60px 70px at 180px 150px,rgba(240,110,160,.9),rgba(240,110,160,0) 100%),radial-gradient(ellipse 60px 50px at 190px 40px,rgba(60,110,200,.6),rgba(60,110,200,0) 100%),linear-gradient(180deg,#4a4649,#2a2729 60%,#1e1c1e)"></div>
  <h3>Rousa3D</h3>
  <p>Have something in mind that you need printed, but don’t have a 3D printer?&nbsp; We can help you design it, and print it for you.</p>
</article>

<footer class="site-footer" role="img" aria-label="Dim photo of people working in a relaxed office"></footer>
<h2 class="nl-title">NEWSLETTER SIGN UP</h2>
<p class="nl-text">Lorem ipsum dolor sit amet, consectetur adipisicing elit,sed do eiusmod ut labore et dolore</p>
<div class="nl-input">Enter your email...</div>
<div class="nl-button">SUBSCRIBE</div>
<div class="social" style="left:536px;background:#3b5a9a"></div>
<div class="social" style="left:582px;background:#3a9ad9"></div>
<div class="social" style="left:627px;background:var(--blue)"></div>
<p class="legal">Copyright © 2018. Rousa Technologies. All Rights Reserved. &nbsp;&nbsp; | &nbsp;&nbsp; Home &nbsp; | &nbsp;&nbsp; About &nbsp;&nbsp; | &nbsp;&nbsp; Solution &nbsp;&nbsp; | &nbsp;&nbsp; Employment &nbsp;&nbsp; | &nbsp;&nbsp; Contact</p>

</body>
</html>
```